Finiding oppertunites in Real Estate 6.15.20

size of ad 7” x 9.6”
1-I like the ad to stand out and attract people's attention.
2-you should be able to see the text of the ad clearly .. see the attachment anything in yellow is instructions.
3-the list of topics should not be the main part of the ad
4-if you decide you want a picture or vector of a person .. (you decide)
then it should be a white male about 25-30 years old wearing a solid white or blue shirt and not long hair.
5-leave 1 inch for footer
see attachment
Good luck

Target Market(s)

potential male students 25-35 years of age

Industry/Entity Type

Education

Requirements
Must have
• will stand out and people would want to see it.
should be able to read the words of ad
Nice to have
• how to make money in real estate on one line

```html
<!DOCTYPE html>
<html lang="en">
<head>
<meta charset="utf-8">
<title>Real Estate Career Course</title>
<link rel="stylesheet" href="https://fonts.googleapis.com/css2?family=Kanit:wght@200;600;700&family=Josefin+Sans:wght@300;400&family=Montserrat:wght@700&display=swap">
<style>
  :root{
    --backdrop:#e2b806;
    --yellow:#fdd80b;
    --navy:#003a49;
    --ink:#0b3a46;
    --white:#ffffff;
    --photo-light:#e7e9ea;
    --photo-mid:#b9bdc0;
  }
  *{margin:0;padding:0;box-sizing:border-box}
  html,body{width:1200px;height:1200px;overflow:hidden}
  body{background:var(--backdrop);position:relative;font-family:"Josefin Sans",sans-serif}
  .flyer{position:absolute;left:200px;top:52px;width:800px;height:1096px;background:var(--yellow);overflow:hidden}
  .flyer > *{position:absolute}
  .header-title{left:0;top:0;width:800px;height:102px;display:flex;align-items:center;justify-content:center;
    font-family:"Kanit",sans-serif;font-weight:700;font-size:48px;color:var(--ink);letter-spacing:-0.5px;line-height:1;padding-top:2px}
  .main-panel{left:0;top:102px;width:800px;height:880px;background:var(--navy)}
  .hero-photo{left:404px;top:102px;width:396px;height:427px;
    background:linear-gradient(100deg,var(--photo-mid) 0%,var(--photo-light) 45%,#f4f5f5 70%,var(--photo-light) 100%)}
  .hero-band{left:710px;top:102px;width:74px;height:427px;background:var(--yellow);opacity:.85}
  .accent-dash{left:25px;height:9px;background:var(--yellow)}
  .dash-1{top:122px;width:41px}
  .dash-2{top:336px;width:41px}
  .dash-3{top:531px;width:54px}
  .headline-lead{left:29px;top:148px;font-weight:300;font-size:45px;color:var(--white);line-height:1;letter-spacing:.5px}
  .headline-money{left:27px;top:192px;font-family:"Kanit",sans-serif;font-weight:700;font-size:76px;color:var(--yellow);line-height:1;letter-spacing:-1.5px}
  .headline-estate{left:27px;top:272px;font-family:"Kanit",sans-serif;font-weight:700;font-size:51px;color:var(--white);line-height:1;letter-spacing:-.5px}
  .intro{left:26px;top:368px;width:352px;color:var(--white);font-size:20.5px;line-height:25px;text-align:justify}
  .intro p + p{margin-top:11px}
  .intro .stretch{text-align-last:justify}
  .topics-heading{left:25px;top:560px;font-family:"Montserrat",sans-serif;font-weight:700;font-size:21px;color:var(--white);line-height:1;letter-spacing:.3px}
  .topics{left:25px;top:596px;list-style:none;color:var(--white);font-size:17.5px;line-height:27px}
  .topics li{display:flex;align-items:center}
  .topics li::before{content:"";width:7px;height:7px;background:var(--yellow);margin-right:10px;margin-top:-4px}
  .session-card{left:400px;top:602px;width:400px;height:380px;background:var(--white);border-top-left-radius:31px;
    display:flex;flex-direction:column;align-items:center;text-align:center;line-height:1}
  .session-remote{margin-top:16px;font-family:"Kanit",sans-serif;font-weight:200;font-size:52px;color:var(--yellow);letter-spacing:1px}
  .session-title{margin-top:4px;font-family:"Kanit",sans-serif;font-weight:700;font-size:64px;color:var(--yellow);letter-spacing:-1px}
  .course-length{margin-top:10px;width:194px;border-top:1.5px solid var(--ink);border-bottom:1.5px solid var(--ink);
    padding:4px 0 6px;font-family:"Kanit",sans-serif;font-weight:700;color:var(--ink)}
  .course-length .count{display:block;font-size:32px;letter-spacing:.5px}
  .course-length .word{display:block;font-size:43px;margin-top:-4px;letter-spacing:.5px}
  .start-label{margin-top:20px;font-family:"Montserrat",sans-serif;font-weight:500;font-size:28px;color:var(--ink);letter-spacing:.3px}
  .start-date{margin-top:8px;font-family:"Kanit",sans-serif;font-weight:700;font-size:58px;color:var(--yellow)}
</style>
</head>
<body>
  <main class="flyer">
    <h1 class="header-title">REAL ESTATE CAREER COURSE</h1>
    <div class="main-panel"></div>
    <div class="hero-photo" role="img" aria-label="Photo of a young man in a white shirt holding a tablet, office building behind him"></div>
    <div class="hero-band"></div>

    <span class="accent-dash dash-1"></span>
    <p class="headline-lead">HOW TO MAKE</p>
    <p class="headline-money">MONEY IN</p>
    <p class="headline-estate">REAL ESTATE?</p>
    <span class="accent-dash dash-2"></span>

    <div class="intro">
      <p><span class="stretch" style="display:block">For those who have started or</span>would like to go into Real Estate.</p>
      <p>An investment in knowledge opens up untold opportunities.</p>
    </div>

    <span class="accent-dash dash-3"></span>
    <h2 class="topics-heading">A PARTIAL LISTING OF TOPICS</h2>
    <ul class="topics">
      <li>Single-family</li>
      <li>Multifamily</li>
      <li>Management</li>
      <li>Real Estate Concepts</li>
      <li>Real Estate law</li>
      <li>Investment properties</li>
      <li>Foreclosures</li>
      <li>Rehab</li>
      <li>Foreclosures</li>
      <li>Short sales</li>
      <li>Development</li>
      <li>Finical modeling</li>
      <li>HUD properties</li>
      <li>Due Diligence</li>
    </ul>

    <section class="session-card">
      <p class="session-remote">REMOTE</p>
      <p class="session-title">SESSIONS</p>
      <p class="course-length"><span class="count">12 SESSION</span><span class="word">COURSE</span></p>
      <p class="start-label">CLASSES STARTING</p>
      <p class="start-date">JUNE 16</p>
    </section>
  </main>
</body>
</html>
```